#1 Selling Sweden weight loss supplement comes to USA - LABEL needed!

The number one weight loss in Sweden is coming to USA

-I need a label that is clean and simple but somehow represents, in an abstract way, weight loss or slender.
-The product and water mixed is all the is needed. This too could be represented in the label design.
-The bottle will be white.

-Attached is a picture of a supplement bottle with
--the logo for the company, 'Kelvora'
--the name of the supplement, 'Quillon Breeze'
and
--other text that could be included in the final label.

ALSO attached are 2 label designs that I like. This might give you an idea of a direction to go.
Thank You very much.

Target Market(s)

Health conscience people

Industry/Entity Type

Weight

Font styles to use
Sans Serif

Requirements
Must have
• -Size of bottle - 2" wide x 4" high
Nice to have
• *Lowers Hunger up to 50%
• *Decreases cravings or unhealthy foods up to 90%
• *Enhances Weight Loss
• " A Zorvanex a day keeps hunger away"

```html
<!DOCTYPE html>
<html lang="en">
<head>
<meta charset="utf-8">
<title>Quillon Breeze Label</title>
<link rel="stylesheet" href="https://fonts.googleapis.com/css2?family=Quicksand:wght@300;400;500&family=Sacramento&display=swap">
<style>
  :root {
    --paper: #ffffff;
    --frame: #c9c9c9;
    --navy: #26337a;
    --bark: #5b3f22;
    --leaf: #8cc63f;
    --band-light: #a8f56c;
    --band-mid: #5fbf3a;
    --band-dark: #0b6a1c;
    --leaf-photo-light: #7fae4a;
    --leaf-photo-dark: #2f5e22;
    --white: #ffffff;
  }
  * { margin: 0; padding: 0; box-sizing: border-box; }
  html, body {
    width: 978px;
    height: 1200px;
    overflow: hidden;
    background: var(--paper);
  }
  .label {
    position: relative;
    width: 978px;
    height: 1200px;
    background: var(--paper);
    font-family: "Quicksand", sans-serif;
  }
  .label-frame {
    position: absolute;
    left: 16px;
    top: 28px;
    width: 948px;
    height: 1164px;
    border: 2px solid var(--frame);
  }
  .brand {
    position: absolute;
    top: 100px;
    left: 0;
    width: 100%;
    display: flex;
    justify-content: center;
    align-items: center;
    gap: 14px;
  }
  .brand-name {
    font-weight: 400;
    font-size: 56px;
    line-height: 1;
    color: var(--navy);
    letter-spacing: 1px;
  }
  .brand-dot {
    width: 18px;
    height: 18px;
    border-radius: 50%;
    background: var(--navy);
  }
  .product-name {
    position: absolute;
    top: 318px;
    left: 0;
    width: 100%;
    text-align: center;
    font-weight: 300;
    font-size: 92px;
    line-height: 1;
    color: var(--bark);
    letter-spacing: 2px;
  }
  .product-subname {
    position: absolute;
    top: 420px;
    left: 0;
    width: 100%;
    text-align: center;
    font-family: "Sacramento", cursive;
    font-size: 92px;
    line-height: 1;
    color: var(--leaf);
  }
  .product-subname sup {
    font-family: "Quicksand", sans-serif;
    font-size: 20px;
    vertical-align: top;
    position: relative;
    top: 18px;
    margin-left: 4px;
  }
  .ingredient {
    position: absolute;
    top: 516px;
    left: 0;
    width: 100%;
    text-align: center;
    font-weight: 300;
    font-size: 32px;
    line-height: 1;
    color: var(--leaf);
    letter-spacing: 1px;
  }
  .ingredient sup { font-size: 16px; vertical-align: top; }
  .benefit-band {
    position: absolute;
    left: 17px;
    top: 734px;
    width: 944px;
    height: 336px;
    background: linear-gradient(90deg, var(--band-light) 0%, var(--band-mid) 50%, var(--band-dark) 100%);
  }
  .product-photo {
    position: absolute;
    left: 364px;
    top: 640px;
    width: 236px;
    height: 180px;
    border-radius: 48% 52% 46% 54% / 50% 44% 56% 50%;
    background: radial-gradient(ellipse at 45% 40%, var(--leaf-photo-light) 0%, var(--leaf-photo-dark) 100%);
  }
  .benefits {
    position: absolute;
    top: 848px;
    left: 0;
    width: 100%;
    list-style: none;
    text-align: center;
    color: var(--white);
    font-weight: 400;
    font-size: 26px;
    line-height: 1.1;
  }
  .benefits li { margin-bottom: 30px; }
  .benefits li.two-line { width: 480px; margin-left: auto; margin-right: auto; }
  .tagline {
    position: absolute;
    top: 1080px;
    left: 0;
    width: 100%;
    text-align: center;
    font-family: "Sacramento", cursive;
    font-size: 46px;
    line-height: 1.2;
    color: var(--leaf);
    letter-spacing: 2px;
  }
</style>
</head>
<body>
  <main class="label">
    <div class="label-frame"></div>

    <header class="brand">
      <span class="brand-name">Kelvora</span>
      <span class="brand-dot"></span>
    </header>

    <h1 class="product-name">Quillon</h1>
    <p class="product-subname">Breeze<sup>®</sup></p>
    <p class="ingredient">W/ PURE ZORVANEX <sup>®</sup></p>

    <div class="benefit-band"></div>
    <div class="product-photo" role="img" aria-label="Photo of fresh spinach leaves"></div>

    <ul class="benefits">
      <li>Lowers Hunger up to 50%</li>
      <li class="two-line">Decreases cravings or unhealthy foods up to 90%</li>
      <li>Enhances Weight Loss</li>
    </ul>

    <p class="tagline">A Zorvanex a day keeps hunger away</p>
  </main>
</body>
</html>
```